1 page flyer / info document for IT services company

We need t one-pager to distribute to clients/potential clients focusing on services that we offer, and how they can benefit. We focus on Desk Suite 88 - deployment, migration and most of all - SECURITY. We want to enlighten them to the fact that Desk Suite 88 is not "secure" unless the appropriate steps have taken place to make it so. The design must reflect the colours and feel of our website. www.taluvex.com.au

Target Market(s)

Professional Services Firms, lawyers, accountants, healthcare professionals

Industry/Entity Type

Professional Service

Requirements
Must have
• We are focusing on Desk Suite 88 - so the big line at the top needs to read "Is your Desk Suite 88 secure? Unless you've customised it for security, the answer is NO". Further text in the attached Word document. (should not be too wordy!). Ideally I'd like a version with a 'customisable" section in the middle where we can insert a relevant case study (based on the industry we are sending it to at that time)
Nice to have
• Images of the Brindlecorp logo and Desk Suite 88. The theme of this flyer is Cyber Security, so any images or text that may enhance that vision.

```html
<!DOCTYPE html>
<html lang="en">
<head>
<meta charset="utf-8">
<title>Taluvex – Is your Desk Suite 88 secure?</title>
<link href="https://fonts.googleapis.com/css2?family=Roboto:wght@400;500;700&display=swap" rel="stylesheet">
<style>
  :root{
    --sky:#29a8e0;
    --sky-deep:#1b8fd0;
    --sky-light:#4bbbeb;
    --navy:#2b2a7d;
    --alert-yellow:#fde012;
    --highlight:#fde012;
    --ink:#111111;
    --white:#ffffff;
    --icon-blue:#3d7cc9;
  }
  *{box-sizing:border-box;margin:0;padding:0}
  html,body{width:865px;height:1200px;overflow:hidden}
  body{font-family:"Roboto",Arial,sans-serif;color:var(--white);background:var(--sky)}
  .flyer{position:relative;width:865px;height:1200px;overflow:hidden}
  .flyer__backdrop{position:absolute;inset:0;
    background:linear-gradient(160deg,var(--sky-deep) 0%,var(--sky) 40%,var(--sky-light) 70%,var(--sky-deep) 100%)}

  .alert-box{position:absolute;left:72px;top:57px;width:726px;height:406px;
    background:var(--alert-yellow);border-radius:4px;color:var(--ink);text-align:center;padding-top:14px}
  .alert-box h2{font-size:27px;font-weight:700;line-height:1.2}
  .alert-box p{font-size:20px;line-height:1.35}
  .alert-box .gap{margin-top:26px}
  .alert-box h2.cta-head{margin-top:22px;line-height:1.25}
  .alert-box .lead{width:640px;margin:0 auto}

  .custom-section{position:absolute;left:0;top:484px;width:865px;text-align:center;font-size:22px;line-height:1.6}
  .custom-section .insert{color:var(--highlight);font-weight:700}
  .product-name{display:inline-flex;align-items:center;gap:6px;color:#e8422b;font-weight:400}
  .product-name::before{content:"";width:18px;height:18px;background:#e8422b;display:inline-block}
  .benefit-question{position:absolute;left:80px;top:574px;width:705px;text-align:center;font-size:18.5px;line-height:1.2}

  .consult-button{position:absolute;left:219px;top:647px;width:431px;height:40px;border:2px solid var(--white);
    border-radius:20px;background:var(--navy);display:flex;align-items:center;justify-content:center;gap:8px;
    font-size:20px;font-weight:700}
  .consult-button svg{width:24px;height:20px}

  .services-rule{position:absolute;left:90px;top:759px;width:692px;height:2px;background:var(--white)}
  .services-tab{position:absolute;left:298px;top:723px;width:273px;height:38px;background:var(--navy);
    border:2px solid var(--white);border-bottom:none;border-radius:8px 8px 0 0;
    font-size:20px;font-weight:500;text-align:center;line-height:36px}

  .service{position:absolute;width:150px;text-align:center}
  .service__card{position:relative;width:142px;height:105px;margin-left:4px}
  .service__card::before{content:"";position:absolute;left:5px;top:-4px;width:142px;height:105px;background:var(--navy)}
  .service__face{position:absolute;inset:0;background:var(--white);display:flex;align-items:center;justify-content:center}
  .service__art{width:88px;height:84px;border-radius:50%}
  .service__art--support{background:radial-gradient(circle,#ffffff 30%,#555 34%,#222 70%)}
  .service__art--backup{border-radius:6px;background:linear-gradient(135deg,#7ec3ee,#9aa4ad 60%,#5b6470)}
  .service__art--hardware{border-radius:6px;background:linear-gradient(135deg,#f4c85a,#c9922a 55%,#9cb6cf)}
  .service__face svg{width:78px;height:84px}
  .service__label{margin-top:6px;font-size:16px;line-height:1.15}

  .footer-band{position:absolute;left:0;top:1118px;width:865px;height:82px}
  .footer-address{position:absolute;left:496px;top:1131px;display:flex;align-items:center;gap:6px;font-size:16px}
  .footer-address svg{width:14px;height:20px}
</style>
</head>
<body>
<main class="flyer">
  <div class="flyer__backdrop" role="img" aria-label="Blue background with a faint geometric triangle pattern"></div>

  <section class="alert-box">
    <h2>Is your Desk Suite 88 secure?</h2>
    <p>If you haven’t taken specific action to improve security, then<br>the answer is NO.</p>
    <p class="gap lead">Desk Suite 88 is arguably the best Business Productivity platform ever created, however ‘out of the box’ it requires customisation to ensure the security of your business.</p>
    <h2 class="cta-head">Want to reduce the risk of Cybercrime affecting<br>your business?</h2>
    <p>Contact us now for a free consultation and security assessment.<br>We will come to you.</p>
  </section>

  <section class="custom-section">
    <p>For the “customisable” version, I’d like to <span class="insert">INSERT CASE STUDY HERE</span></p>
    <p>are you not using <span class="product-name">Desk Suite 88</span> yet?</p>
  </section>

  <p class="benefit-question">Would you like to know how it can increase productivity, reduce risk, and increase overall profitability of your business?</p>

  <div class="consult-button">
    <svg viewBox="0 0 24 20" aria-hidden="true"><path fill="#29a8e0" d="M2 6c0-3 5-5 10-5s10 2 10 5l-1 2h-4l-1-3H8L7 8H3zM6 10l2-3h8l2 3v8H6z"/><circle cx="12" cy="13" r="2.5" fill="#2b2a7d"/></svg>
    Contact us for a free consultation.
  </div>

  <div class="services-rule"></div>
  <h3 class="services-tab">Other services we offer</h3>

  <div class="service" style="left:85px;top:787px">
    <div class="service__card"><div class="service__face"><div class="service__art service__art--support" role="img" aria-label="24/7 service clock badge"></div></div></div>
    <p class="service__label">24/7<br>IT Support</p>
  </div>
  <div class="service" style="left:268px;top:787px">
    <div class="service__card"><div class="service__face"><div class="service__art service__art--backup" role="img" aria-label="Computers backing up to a cloud and a safe"></div></div></div>
    <p class="service__label">Backup and<br>Disaster Recovery</p>
  </div>
  <div class="service" style="left:450px;top:787px">
    <div class="service__card"><div class="service__face">
      <svg viewBox="0 0 78 84" aria-hidden="true" fill="none" stroke="#3d7cc9" stroke-width="3">
        <path d="M14 6h50l6 14H8z"/><rect x="8" y="20" width="62" height="14"/><rect x="8" y="34" width="62" height="14"/><rect x="8" y="48" width="62" height="12"/>
        <path d="M46 27h16M46 41h16M46 54h16M39 60v10M14 76h50"/><circle cx="39" cy="76" r="4"/>
      </svg>
    </div></div>
    <p class="service__label">IT<br>Strategy</p>
  </div>
  <div class="service" style="left:635px;top:787px">
    <div class="service__card"><div class="service__face"><div class="service__art service__art--hardware" role="img" aria-label="Software box with a disc"></div></div></div>
    <p class="service__label">Hardware and<br>Software Sales</p>
  </div>
  <div class="service" style="left:360px;top:960px">
    <div class="service__card"><div class="service__face">
      <svg viewBox="0 0 78 84" aria-hidden="true" fill="none" stroke="#3d7cc9" stroke-width="3">
        <rect x="8" y="8" width="16" height="66" rx="3"/><rect x="24" y="14" width="46" height="60" rx="3"/>
        <rect x="32" y="22" width="30" height="14"/>
        <g fill="#3d7cc9" stroke="none"><rect x="32" y="44" width="7" height="6"/><rect x="44" y="44" width="7" height="6"/><rect x="56" y="44" width="7" height="6"/><rect x="32" y="54" width="7" height="6"/><rect x="44" y="54" width="7" height="6"/><rect x="56" y="54" width="7" height="6"/><rect x="32" y="64" width="7" height="5"/><rect x="44" y="64" width="7" height="5"/><rect x="56" y="64" width="7" height="5"/></g>
      </svg>
    </div></div>
    <p class="service__label">Telephony</p>
  </div>

  <svg class="footer-band" viewBox="0 0 865 82" preserveAspectRatio="none" aria-hidden="true">
    <path d="M290 82 C 300 30, 320 2, 380 2 L865 2 L865 82 Z" fill="#ffffff"/>
    <path d="M296 82 C 306 34, 326 6, 384 6 L865 6 L865 82 Z" fill="#2b2a7d"/>
  </svg>
  <p class="footer-address">
    <svg viewBox="0 0 14 20" aria-hidden="true"><path fill="#fde012" d="M7 0a7 7 0 0 0-7 7c0 5 7 13 7 13s7-8 7-13a7 7 0 0 0-7-7z"/><circle cx="7" cy="7" r="2.6" fill="#2b2a7d"/></svg>
    Level 3, 212 Harrow St.&nbsp; Eastvale.&nbsp; 3000
  </p>
</main>
</body>
</html>
```